Dune Air & Plus business card

I need an awesome, double-sided business card designed with our new logo. I would like the one side black with the colored logo, and the back side is all yours. I'd like to see horizontal and vertical layouts. Get creative! Thank you.

Target Market(s)

HVAC, Heating and Cooling in Phoenix, AZ

Industry/Entity Type

HVAC

Contact Information for Business Card

We need our new logo on the card. Tom Harker, (623) 555-0142, tom@trydunesair.com, www.trydunesair.com, ROC 514273

```html
<!DOCTYPE html>
<html lang="en">
<head>
<meta charset="utf-8">
<title>Dune Air &amp; Plus – Business Card</title>
<link rel="stylesheet" href="https://fonts.googleapis.com/css2?family=Montserrat:wght@300;400;700;800&display=swap">
<style>
  :root {
    --bg: #d3d3d3;
    --card-dark-top: #363538;
    --card-dark-bottom: #262527;
    --brand-blue: #1771bb;
    --brand-blue-deep: #1f5fae;
    --brand-orange: #f58220;
    --white: #ffffff;
    --shadow: rgba(0, 0, 0, 0.28);
  }
  * { box-sizing: border-box; margin: 0; padding: 0; }
  html, body {
    width: 668px; height: 1200px; overflow: hidden;
    background: var(--bg);
    font-family: "Montserrat", sans-serif;
  }
  .stage {
    position: relative; width: 668px; height: 1200px;
  }
  .card {
    position: absolute; top: 355px;
    width: 280px; height: 490px;
    box-shadow: 0 6px 10px var(--shadow);
    overflow: hidden;
  }
  /* Front side */
  .card-front {
    left: 39px;
    background: linear-gradient(180deg, var(--card-dark-top) 0%, var(--card-dark-bottom) 100%);
  }
  .faint-decor {
    position: absolute; border-radius: 50%;
  }
  .faint-decor--cool {
    left: 0; top: 0; width: 96px; height: 92px;
    background: radial-gradient(circle, rgba(255,255,255,0.05) 0%, rgba(255,255,255,0) 70%);
  }
  .faint-decor--warm {
    right: 0; bottom: 0; width: 90px; height: 110px;
    background: radial-gradient(circle, rgba(0,0,0,0.14) 0%, rgba(0,0,0,0) 70%);
  }
  .brand-mark {
    position: absolute; left: 0; right: 0;
    display: flex; align-items: center; justify-content: center; gap: 8px;
    font-weight: 800; letter-spacing: 0.3px; white-space: nowrap;
  }
  .card-front .brand-mark {
    top: 234px; font-size: 21px; color: var(--brand-orange);
  }
  .brand-dot {
    width: 12px; height: 12px; border-radius: 50%;
    background: var(--brand-blue);
    flex: none;
  }
  /* Back side */
  .card-back {
    left: 349px; background: var(--white);
  }
  .card-back .brand-mark {
    top: 96px; left: 22px; right: auto; width: 170px;
    font-size: 19px; color: var(--brand-blue-deep);
  }
  .card-back .brand-dot { background: var(--brand-orange); }
  .contact-band {
    position: absolute; left: 0; right: 0; top: 224px; bottom: 0;
    background: var(--brand-blue);
  }
  .band-notch {
    position: absolute; left: 46px; top: -1px;
  }
  .person-name {
    position: absolute; left: 44px; top: 60px;
    color: var(--white); font-weight: 700; font-size: 21px; line-height: 1;
  }
  .license {
    position: absolute; left: 44px; top: 86px;
    color: var(--white); font-weight: 400; font-size: 14px; line-height: 1;
  }
  .contact-list {
    position: absolute; left: 44px; top: 138px;
    list-style: none;
  }
  .contact-item {
    display: flex; align-items: center; height: 19px;
    color: var(--white); font-weight: 300; font-size: 12.5px;
  }
  .contact-icon {
    width: 11px; height: 11px; margin-right: 12px; flex: none;
  }
</style>
</head>
<body>
<main class="stage">
  <section class="card card-front" aria-label="Business card front">
    <div class="faint-decor faint-decor--cool" role="img" aria-label="Faint snowflake decoration"></div>
    <div class="faint-decor faint-decor--warm" role="img" aria-label="Faint flame decoration"></div>
    <div class="brand-mark"><span class="brand-dot"></span>Dune Air &amp; Plus</div>
  </section>

  <section class="card card-back" aria-label="Business card back">
    <div class="brand-mark"><span class="brand-dot"></span>Dune Air &amp; Plus</div>
    <div class="contact-band">
      <svg class="band-notch" width="20" height="9" viewBox="0 0 20 9" aria-hidden="true">
        <polygon points="0,0 20,0 10,9" fill="#ffffff"/>
      </svg>
      <h1 class="person-name">Tom Harker</h1>
      <p class="license">ROC 514273</p>
      <ul class="contact-list">
        <li class="contact-item">
          <svg class="contact-icon" viewBox="0 0 24 24" aria-hidden="true">
            <path fill="#f58220" d="M6.6 10.8a15.1 15.1 0 0 0 6.6 6.6l2.2-2.2c.3-.3.7-.4 1-.2 1.1.4 2.3.6 3.6.6.6 0 1 .4 1 1V20c0 .6-.4 1-1 1A17 17 0 0 1 3 4c0-.6.4-1 1-1h3.5c.6 0 1 .4 1 1 0 1.3.2 2.5.6 3.6.1.3 0 .7-.2 1z"/>
          </svg>(623) 555-0142
        </li>
        <li class="contact-item">
          <svg class="contact-icon" viewBox="0 0 24 24" aria-hidden="true">
            <rect x="2" y="5" width="20" height="14" rx="1.5" fill="#f58220"/>
            <polyline points="2.5,6 12,13 21.5,6" fill="none" stroke="#1771bb" stroke-width="1.6"/>
          </svg>tom@trydunesair.com
        </li>
        <li class="contact-item">
          <svg class="contact-icon" viewBox="0 0 24 24" aria-hidden="true">
            <circle cx="12" cy="12" r="10" fill="#f58220"/>
            <path d="M2 12h20M12 2c3 3 3 17 0 20M12 2c-3 3-3 17 0 20" fill="none" stroke="#1771bb" stroke-width="1.3"/>
          </svg>www.trydunesair.com
        </li>
      </ul>
    </div>
  </section>
</main>
</body>
</html>
```